Medical Cannabis company is looking for a LOGO design *

SILVER PETALWORKS (SP) is a new company in the Israeli medical cannabis industry. We will engage in PREMIUM medical cannabis growing and cultivation and also manufacturing of HIGH-END cannabis based medical products.
the design should reflect luxury, high-end and Pharma-grade products.
the design should use color GOLD and NOT using the famous cannabis leaf !

Target Market(s)

international medical cannabis Pharmaceutical companies
and of course local and international patients

Contact Information for Business Card

Yoav Ben-Ami
Founder and CEO

Silver Petalworks
Medical grade cannabis

yoavbenami@mailnest.example
972-52-3186907

Colors
ffc214
fbed22

Requirements
Must have
• clean and simple
• luxury
• gold !!
• (can also have green for Cannabis and/or blue for Pharma)
Should not have
• cannabis leaf

```html
<!DOCTYPE html>
<html lang="en">
<head>
<meta charset="utf-8">
<title>Silver Petalworks – Business Card</title>
<link rel="stylesheet" href="https://fonts.googleapis.com/css2?family=Source+Sans+3:wght@400;600;700&display=swap">
<style>
  :root {
    --backdrop: #8ccfd1;
    --card: #2b2b2c;
    --gold: #c99253;
    --gold-soft: #b9874e;
  }
  html, body {
    margin: 0;
    padding: 0;
    width: 1200px;
    height: 956px;
    overflow: hidden;
    background: var(--backdrop);
  }
  .canvas {
    position: relative;
    width: 1200px;
    height: 956px;
  }
  .card {
    position: absolute;
    left: 50px;
    top: 160px;
    width: 1100px;
    height: 636px;
    background: var(--card);
    font-family: "Source Sans 3", "Source Sans Pro", sans-serif;
    color: var(--gold);
  }
  .brand {
    position: absolute;
    right: 72px;
    top: 72px;
    text-align: right;
  }
  .brand-name {
    display: block;
    font-size: 48px;
    font-weight: 700;
    line-height: 1;
    letter-spacing: -0.5px;
  }
  .brand-tagline {
    display: block;
    margin-top: 4px;
    font-size: 17px;
    font-weight: 400;
    letter-spacing: 5.4px;
    margin-right: -5px;
  }
  .person {
    position: absolute;
    left: 54px;
    top: 302px;
  }
  .person-name {
    display: block;
    font-size: 22px;
    font-weight: 700;
    letter-spacing: 6px;
  }
  .person-role {
    display: block;
    margin-top: 4px;
    font-size: 18px;
    font-weight: 400;
    letter-spacing: 4.6px;
    color: var(--gold-soft);
  }
  .contacts {
    position: absolute;
    left: 54px;
    top: 405px;
    margin: 0;
    padding: 0;
    list-style: none;
  }
  .contact {
    display: flex;
    align-items: center;
    height: 41px;
    font-size: 18px;
    font-weight: 600;
    letter-spacing: 5px;
  }
  .contact-icon {
    width: 22px;
    height: 22px;
    margin-right: 22px;
    fill: var(--gold);
  }
</style>
</head>
<body>
<div class="canvas">
  <section class="card">
    <div class="brand">
      <span class="brand-name">Silver Petalworks</span>
      <span class="brand-tagline">MEDICAL GRADE CANNABIS</span>
    </div>

    <div class="person">
      <span class="person-name">YOAV BEN-AMI</span>
      <span class="person-role">FOUNDER AND CEO</span>
    </div>

    <ul class="contacts">
      <li class="contact">
        <svg class="contact-icon" viewBox="0 0 24 24" aria-hidden="true">
          <path d="M2 5h20v14H2z M3.5 6.5 12 13l8.5-6.5" fill="none" stroke="#c99253" stroke-width="0"/>
          <path d="M2 5h20v14H2V5zm1.8 1.5L12 12.6l8.2-6.1H3.8zM3.5 8.2v9.3h17V8.2L12 14.5 3.5 8.2z"/>
        </svg>
        YOAVBENAMI@MAILNEST.EXAMPLE
      </li>
      <li class="contact">
        <svg class="contact-icon" viewBox="0 0 24 24" aria-hidden="true">
          <circle cx="12" cy="12" r="9" fill="none" stroke="#c99253" stroke-width="2"/>
          <path d="M3 12h18M12 3c3 3 3 15 0 18M12 3c-3 3-3 15 0 18" fill="none" stroke="#c99253" stroke-width="1.6"/>
        </svg>
        WWW.SILVERPETALWORKS.EXAMPLE
      </li>
      <li class="contact">
        <svg class="contact-icon" viewBox="0 0 24 24" aria-hidden="true">
          <path d="M6.6 10.8a15.1 15.1 0 0 0 6.6 6.6l2.2-2.2c.3-.3.7-.4 1-.2 1.1.4 2.3.6 3.6.6.6 0 1 .4 1 1V20c0 .6-.4 1-1 1A17 17 0 0 1 3 4c0-.6.4-1 1-1h3.5c.6 0 1 .4 1 1 0 1.3.2 2.5.6 3.6.1.3 0 .7-.2 1l-2.3 2.2z"/>
        </svg>
        972-52-3186907
      </li>
      <li class="contact">
        <svg class="contact-icon" viewBox="0 0 24 24" aria-hidden="true">
          <path d="M12 2a7 7 0 0 0-7 7c0 5.2 7 13 7 13s7-7.8 7-13a7 7 0 0 0-7-7zm0 9.5A2.5 2.5 0 1 1 12 6.5a2.5 2.5 0 0 1 0 5z"/>
        </svg>
        27 OLIVE GROVE STREET MODIIN | ISRAEL
      </li>
    </ul>
  </section>
</div>
</body>
</html>
```